Healthy Snack Bar Wrapper Design

We are passionate about delivering healthy and tasty treats that are Raw, Organic, Preservative Free, Gluten Free, have No Added Sugar and No Additives!
In this project we are looking for a design for a new healthy food product to be launched soon in Australia. The packaging will be a bar wrapper made from foil that will be hot sealed, with a front and a back.
The snack is a raw, organic and healthy treat made predominantly with nuts, and will come in 3 initial flavours:
- Black Forest (Sour Cherry and Choc)
- Plum Fandango (Banana, Apricot and Blueberry)
- Zestivelle (Pineapple, Passionfruit and Kiwi)
The product name is NibbleMoss, which does not currently have a logo. We are happy to have this as a simple written component of the initial design at the top of the packaging, perhaps within an circle, square or oval.
The typeface used for the names and the main ingredients should be fun.
The overall design should be very simple and make use of minimal colours. Our preferences are to have a plain colour for the background, such as light organic brown or white, with an eye catching colour that can be used to define the flavour, but should not be too vibrant.
We do not want to have an 3 dimensional images or objects. Nor do we want to have product images and any imagery should be only to give the impression of the flavours within rather than an image of the flavour. Finally, we do not want to have gradients included in the design.
The final design should communicate healthy, tasty and fun!
Examples of inspiration designs are attached in the files.
Main Information:
- The front should comprise of the following information:
-- NibbleMoss
-- Flavour name (such as Black Forest)
-- Main Ingredients (Sour Cherry and Choc) (This is optional)
-- Portion size (60g)
-- Message (This is optional)
--- 0% Additives
--- 60% Nuts
--- 100% Natural
- The back needs to have space for the following information:
-- Nutritional Information
-- Barcode
-- Ingredients
-- Contact information
- Wrapper Dimensions
-- Width: 14cm
-- Height: 15cm
- Bar Dimensions
-- Width: 3cm
-- Height: 10cm
-- Depth: 2.5cm
Target Market(s)
People who want to have a healthy tasty treat
Colors
Designer to choose colors to be used in the design.
Requirements
Must have
- Main Information:
- - The front should comprise of the following information:
- -- NibbleMoss
- -- Flavour name (such as Black Forest)
- -- Main Ingredients (Sour Cherry and Choc) (This is optional)
- -- Portion size (60g)
- -- Message (This is optional)
- --- 0% Additives
- --- 60% Nuts
- --- 100% Natural
- - The back needs to have space for the following information:
- -- Nutritional Information
- -- Barcode
- -- Ingredients
- -- Contact information
- - Wrapper Dimensions
- -- Width: 14cm
- -- Height: 15cm
- - Bar Dimensions
- -- Width: 3cm
- -- Height: 10cm
- -- Depth: 2.5cm
Should not have
- We do not want to have an 3 dimensional images or objects. Nor do we want to have product images and any imagery should be only to give the impression of the flavours within rather than an image of the flavour. Finally, we do not want to have gradients included in the design.

```html
<!DOCTYPE html>
<html lang="en">
<head>
<meta charset="utf-8">
<title>NibbleMoss Snack Bar Wrappers</title>
<link href="https://fonts.googleapis.com/css2?family=Comic+Neue:wght@400;700&display=swap" rel="stylesheet">
<style>
  :root {
    --page-bg: #e9e9ea;
    --wrapper-white: #ffffff;
    --cherry: #5c1b3d;
    --plum: #393c69;
    --zest: #e8952e;
    --label-text: #ffffff;
    --font-fun: "Comic Neue", "Comic Sans MS", cursive;
  }
  * { margin: 0; padding: 0; box-sizing: border-box; }
  html, body { width: 1200px; height: 597px; overflow: hidden; }
  body {
    background: var(--page-bg);
    font-family: var(--font-fun);
  }
  .lineup {
    position: relative;
    width: 1200px;
    height: 597px;
    display: flex;
    justify-content: center;
    align-items: center;
    gap: 90px;
  }
  .wrapper {
    position: relative;
    width: 250px;
    height: 500px;
  }
  .wrapper--cherry { --flavour: var(--cherry); }
  .wrapper--plum { --flavour: var(--plum); }
  .wrapper--zest { --flavour: var(--zest); }
  .wrapper__shape {
    position: absolute;
    inset: 0;
    width: 250px;
    height: 500px;
  }
  .wrapper__content {
    position: absolute;
    inset: 0;
    text-align: center;
    color: var(--label-text);
  }
  .brand-name {
    position: absolute;
    top: 52px;
    left: 0;
    right: 0;
    font-size: 34px;
    font-weight: 700;
    color: var(--label-text);
    letter-spacing: 0.5px;
  }
  .flavour-name {
    position: absolute;
    top: 128px;
    left: 0;
    right: 0;
    font-size: 27px;
    font-weight: 400;
  }
  .flavour-ingredients {
    position: absolute;
    top: 164px;
    left: 0;
    right: 0;
    font-size: 13px;
  }
  .tagline {
    position: absolute;
    top: 205px;
    left: 0;
    right: 0;
    font-size: 54px;
    line-height: 0.98;
    font-weight: 400;
  }
  .claims {
    position: absolute;
    top: 412px;
    left: 0;
    right: 0;
    font-size: 11px;
    font-weight: 700;
    color: var(--flavour);
  }
  .portion {
    position: absolute;
    top: 430px;
    left: 0;
    right: 0;
    font-size: 12px;
    font-weight: 700;
    color: var(--flavour);
  }
</style>
</head>
<body>
<main class="lineup">

  <article class="wrapper wrapper--cherry">
    <svg class="wrapper__shape" viewBox="0 0 250 500" aria-hidden="true">
      <defs>
        <pattern id="seal-cherry" width="10" height="10" patternUnits="userSpaceOnUse">
          <polygon points="0,10 5,0 10,10" fill="#5c1b3d"/>
        </pattern>
        <pattern id="seal-white-1" width="10" height="10" patternUnits="userSpaceOnUse">
          <polygon points="0,0 5,10 10,0" fill="#ffffff"/>
        </pattern>
      </defs>
      <rect x="0" y="0" width="250" height="10" fill="url(#seal-cherry)"/>
      <rect x="0" y="10" width="250" height="380" fill="#5c1b3d"/>
      <path d="M0,385 L20,378 L35,388 L55,372 L70,380 L95,370 L110,382 L130,374 L150,386 L170,370 L190,380 L210,372 L230,384 L250,376 L250,490 L0,490 Z" fill="#ffffff"/>
      <rect x="0" y="490" width="250" height="10" fill="url(#seal-white-1)"/>
    </svg>
    <div class="wrapper__content">
      <p class="brand-name">NibbleMoss</p>
      <h2 class="flavour-name">Black Forest</h2>
      <p class="flavour-ingredients">Sour Cherry &amp; Choc</p>
      <p class="tagline">Taste<br>of<br>Health</p>
      <p class="claims">0% Additives | 60% Nuts | 100% Natural</p>
      <p class="portion">60g</p>
    </div>
  </article>

  <article class="wrapper wrapper--plum">
    <svg class="wrapper__shape" viewBox="0 0 250 500" aria-hidden="true">
      <defs>
        <pattern id="seal-plum" width="10" height="10" patternUnits="userSpaceOnUse">
          <polygon points="0,10 5,0 10,10" fill="#393c69"/>
        </pattern>
        <pattern id="seal-white-2" width="10" height="10" patternUnits="userSpaceOnUse">
          <polygon points="0,0 5,10 10,0" fill="#ffffff"/>
        </pattern>
      </defs>
      <rect x="0" y="0" width="250" height="10" fill="url(#seal-plum)"/>
      <rect x="0" y="10" width="250" height="380" fill="#393c69"/>
      <path d="M0,378 L18,386 L40,372 L60,384 L78,374 L100,388 L122,371 L140,380 L162,373 L180,387 L200,375 L222,383 L250,372 L250,490 L0,490 Z" fill="#ffffff"/>
      <rect x="0" y="490" width="250" height="10" fill="url(#seal-white-2)"/>
    </svg>
    <div class="wrapper__content">
      <p class="brand-name">NibbleMoss</p>
      <h2 class="flavour-name">Plum Fandango</h2>
      <p class="flavour-ingredients">Banana, Apricot &amp; Blueberry</p>
      <p class="tagline">Taste<br>of<br>Health</p>
      <p class="claims">0% Additives | 60% Nuts | 100% Natural</p>
      <p class="portion">60g</p>
    </div>
  </article>

  <article class="wrapper wrapper--zest">
    <svg class="wrapper__shape" viewBox="0 0 250 500" aria-hidden="true">
      <defs>
        <pattern id="seal-zest" width="10" height="10" patternUnits="userSpaceOnUse">
          <polygon points="0,10 5,0 10,10" fill="#e8952e"/>
        </pattern>
        <pattern id="seal-white-3" width="10" height="10" patternUnits="userSpaceOnUse">
          <polygon points="0,0 5,10 10,0" fill="#ffffff"/>
        </pattern>
      </defs>
      <rect x="0" y="0" width="250" height="10" fill="url(#seal-zest)"/>
      <rect x="0" y="10" width="250" height="380" fill="#e8952e"/>
      <path d="M0,382 L22,372 L42,386 L60,376 L84,388 L104,370 L126,382 L146,374 L164,386 L186,372 L206,384 L228,374 L250,384 L250,490 L0,490 Z" fill="#ffffff"/>
      <rect x="0" y="490" width="250" height="10" fill="url(#seal-white-3)"/>
    </svg>
    <div class="wrapper__content">
      <p class="brand-name">NibbleMoss</p>
      <h2 class="flavour-name">Zestivelle</h2>
      <p class="flavour-ingredients">Pineapple, Passionfruit &amp; Kiwi</p>
      <p class="tagline">Taste<br>of<br>Health</p>
      <p class="claims">0% Additives | 60% Nuts | 100% Natural</p>
      <p class="portion">60g</p>
    </div>
  </article>

</main>
</body>
</html>
```